Tarvel Ridge LLC

Need Professional Business cards for New Investment Fund

Target Market(s)

High Quality investors

Industry/Entity Type

Financial

Contact Information for Business Card

Phone Number +1 555 284 6193
Name Pavel Orlinsky
Title Fund Manager
email po@FundTarvel.example
Website www.FundTarvel.example

Colors

Designer to choose colors to be used in the design.

Requirements
Must have
• Must have our Logo and all of the above. Must be made so lettering and loge can be raised

```html
<!DOCTYPE html>
<html lang="en">
<head>
<meta charset="utf-8">
<title>Tarvel Ridge LLC — Business Card</title>
<link rel="stylesheet" href="https://fonts.googleapis.com/css2?family=Montserrat:wght@600&family=Questrial&display=swap">
<style>
  :root {
    --stage: #3a3b3d;
    --forest: #434f41;
    --leaf: #57b947;
    --paper: #ffffff;
    --ink: #3c3c3c;
    --rule: #8a8a8a;
  }
  * { box-sizing: border-box; margin: 0; padding: 0; }
  html, body { width: 1200px; height: 874px; overflow: hidden; }
  body {
    background: var(--stage);
    font-family: "Questrial", "Century Gothic", sans-serif;
    position: relative;
  }
  .card {
    position: absolute;
    left: 330px;
    width: 540px;
    height: 309px;
    border-radius: 22px;
    overflow: hidden;
  }
  .card--back { top: 110px; background: var(--forest); }
  .card--front { top: 453px; background: var(--paper); }

  .brand {
    position: absolute;
    display: flex;
    align-items: center;
    gap: 10px;
    font-family: "Questrial", "Century Gothic", sans-serif;
    font-size: 26px;
    letter-spacing: 0.5px;
    white-space: nowrap;
  }
  .brand__mark { width: 16px; height: 16px; background: var(--leaf); flex: none; }
  .card--back .brand { left: 50%; top: 50%; transform: translate(-50%, -50%); color: var(--paper); }
  .card--front .brand { left: 40px; top: 50%; transform: translateY(-50%); color: var(--forest); font-size: 22px; }

  .divider {
    position: absolute;
    left: 262px;
    top: 62px;
    width: 1px;
    height: 185px;
    background: var(--rule);
  }
  .details { position: absolute; left: 290px; top: 70px; }
  .details__name {
    font-family: "Montserrat", sans-serif;
    font-weight: 600;
    font-size: 21px;
    color: var(--leaf);
    letter-spacing: 0.5px;
    text-transform: uppercase;
  }
  .details__title { font-size: 15px; color: var(--ink); margin-top: 2px; }
  .contact { list-style: none; margin-top: 30px; }
  .contact__item {
    display: flex;
    align-items: center;
    gap: 10px;
    font-size: 14px;
    color: var(--ink);
    line-height: 22px;
  }
  .contact__icon { width: 12px; height: 12px; flex: none; }
</style>
</head>
<body>
  <section class="card card--back" aria-label="Card back">
    <div class="brand"><span class="brand__mark"></span>Tarvel Ridge LLC</div>
  </section>

  <section class="card card--front" aria-label="Card front">
    <div class="brand"><span class="brand__mark"></span>Tarvel Ridge LLC</div>
    <div class="divider"></div>
    <div class="details">
      <p class="details__name">Pavel Orlinsky</p>
      <p class="details__title">Fund Manager</p>
      <ul class="contact">
        <li class="contact__item">
          <svg class="contact__icon" viewBox="0 0 12 12"><path d="M2.5 1 L4.5 3.5 L3.5 4.8 Q5 7.2 7.2 8.5 L8.5 7.5 L11 9.5 L9.8 11 Q5.5 11 1 2.2 Z" fill="#57b947"/></svg>
          +1 555 284 6193
        </li>
        <li class="contact__item">
          <svg class="contact__icon" viewBox="0 0 12 12"><rect x="0.75" y="2.25" width="10.5" height="7.5" fill="none" stroke="#57b947" stroke-width="1.3"/><path d="M0.75 2.25 L6 6.5 L11.25 2.25" fill="none" stroke="#57b947" stroke-width="1.3"/></svg>
          po@FundTarvel.example
        </li>
        <li class="contact__item">
          <svg class="contact__icon" viewBox="0 0 12 12"><circle cx="6" cy="6" r="5.2" fill="none" stroke="#57b947" stroke-width="1.2"/><ellipse cx="6" cy="6" rx="2.3" ry="5.2" fill="none" stroke="#57b947" stroke-width="1"/><path d="M0.8 6 H11.2 M1.8 3.5 H10.2 M1.8 8.5 H10.2" stroke="#57b947" stroke-width="0.9"/></svg>
          www.FundTarvel.example
        </li>
      </ul>
    </div>
  </section>
</body>
</html>
```